Leadership Seminar Concept

We want the theme picture/design of the Leadership Seminar Flyer with theme "Inspiring Commitment"

Industry/Entity Type

Leadership

```html
<!DOCTYPE html>
<html lang="en">
<head>
<meta charset="utf-8">
<title>Inspiring Commitment – Leadership Seminar</title>
<link rel="stylesheet" href="https://fonts.googleapis.com/css2?family=Roboto+Condensed:wght@400;700&family=Mukta:wght@700&family=Raleway:wght@400&family=Marck+Script&display=swap">
<style>
  :root {
    --page-bg: #e4e4e4;
    --sky-top: #0e1c2e;
    --sky-mid: #26476a;
    --sky-low: #5d7f9c;
    --glow: #fbe9b4;
    --glow-warm: #f2c98a;
    --accent: #f4ec1a;
    --ink-light: #ffffff;
    --banner: #07112a;
  }
  * { margin: 0; padding: 0; box-sizing: border-box; }
  html, body {
    width: 1200px;
    height: 1200px;
    overflow: hidden;
    background: var(--page-bg);
  }
  .flyer {
    position: absolute;
    left: 0;
    top: 138px;
    width: 1200px;
    height: 924px;
    overflow: hidden;
    color: var(--ink-light);
  }
  .flyer__backdrop {
    position: absolute;
    inset: 0;
    background:
      radial-gradient(ellipse 420px 300px at 63% 84%, var(--glow) 0%, rgba(242,201,138,0.75) 35%, rgba(242,201,138,0) 75%),
      radial-gradient(ellipse 700px 260px at 30% 90%, rgba(140,168,190,0.55) 0%, rgba(140,168,190,0) 80%),
      linear-gradient(180deg, var(--sky-top) 0%, #1a3350 30%, var(--sky-mid) 55%, var(--sky-low) 80%, #3e5a74 100%);
  }
  .title-box {
    position: absolute;
    left: 66px;
    top: 74px;
    width: 1074px;
    height: 121px;
    border: 1.5px solid rgba(255,255,255,0.85);
    text-align: center;
  }
  .title-box__title {
    font-family: "Roboto Condensed", sans-serif;
    font-weight: 400;
    font-size: 66px;
    line-height: 1;
    letter-spacing: 0.5px;
    margin-top: 24px;
  }
  .title-box__subtitle {
    font-family: "Roboto Condensed", sans-serif;
    font-weight: 700;
    font-size: 17px;
    margin-top: 3px;
  }
  .point {
    position: absolute;
    top: 264px;
    width: 497px;
  }
  .point--left { left: 63px; }
  .point--right { left: 640px; width: 495px; }
  .point__heading {
    display: flex;
    gap: 10px;
    font-family: "Mukta", sans-serif;
    font-weight: 700;
    font-size: 17.5px;
    line-height: 22px;
    color: var(--accent);
    height: 66px;
  }
  .point__arrow { flex: none; width: 16px; height: 14px; margin-top: 4px; }
  .point__body {
    font-family: "Raleway", sans-serif;
    font-size: 16.5px;
    line-height: 21.7px;
    text-align: justify;
  }
  .closing {
    position: absolute;
    left: 100px;
    top: 801px;
    width: 1030px;
    height: 96px;
    background: var(--banner);
    border: 1px solid var(--accent);
    border-radius: 6px;
    font-family: "Marck Script", cursive;
    font-size: 30px;
    line-height: 44px;
    color: var(--accent);
    text-align: center;
    padding-top: 4px;
  }
</style>
</head>
<body>
  <main class="flyer">
    <div class="flyer__backdrop" role="img" aria-label="Businessman with briefcase walking toward a sunlit city skyline under a cloudy blue sky, reflected in water"></div>

    <header class="title-box">
      <h1 class="title-box__title">INSPIRING COMMITMENT</h1>
      <p class="title-box__subtitle">Shifting self, your people and your organization from static to movement to momentum</p>
    </header>

    <section class="point point--left">
      <h2 class="point__heading">
        <svg class="point__arrow" viewBox="0 0 16 14"><path d="M0 0 L16 7 L0 14 L5 7 Z" fill="#f4ec1a"/></svg>
        <span>Inspiring commitment is enabling others to act.</span>
      </h2>
      <p class="point__body">It involves energizing individuals to strive towards a compelling vision of the future, guiding people through change, keeping everyone aligned, building trust and open channels of communication, while reinforcing success.</p>
    </section>

    <section class="point point--right">
      <h2 class="point__heading">
        <svg class="point__arrow" viewBox="0 0 16 14"><path d="M0 0 L16 7 L0 14 L5 7 Z" fill="#f4ec1a"/></svg>
        <span>Shiftability is responding to outward demands from inward strength, purpose and skill.</span>
      </h2>
      <p class="point__body">The mindset of shiftability acknowledges the need for change and embraces it, keeping an open mind about new ideas while wisely retaining things that still apply- always learning, always building, always growing.</p>
    </section>

    <p class="closing">We invite you to a journey of greatness where you'll learn and practice tools<br>for thriving as a leader by inspiring momentum.</p>
  </main>
</body>
</html>
```